A landing page- for our luxury toothbrush company called "Vörn"

A landing page to gain interest, traction, and potentially presales for our luxury toothbrush brand Vörn. I would like something like this -- does not have to be exact
LANDING PAGE OUTLINE
1️⃣ HERO SECTION (Above the Fold)
Headline:
Rethink Your Daily Hollow.
Subheadline:
A luxury, refillable toothbrush designed with intention — where beauty meets dentistry.
Buttons:
Join the Founding List or Email list
Link to complete survey for 20% off first purchase
Small line underneath:
Launching Fall 2026 · Limited Keeper’s Edition
2️⃣ THE PROBLEM (Emotional Framing)
Headline:
Oral care hasn’t evolved like beauty has.
Copy:
We invest in skincare rituals.
We curate our bathrooms.
We obsess over packaging and detail.
Yet the toothbrush — something we use twice daily — remains clinical, disposable, and uninspired.
You deserve better.
3️⃣ THE PRODUCT (Your Differentiation)
Headline:
Designed to be Displayed. Engineered to Perform.
Bullets (Luxury + Function):
• Hand-finished premium prints on an acetate handle
• Slim sculptural silhouette
• Gold-accent detailing
• Replaceable brush head system
• Premium bristles (dentist-selected)
• Designed by a practicing dentist
- Custom engraving
4️⃣ THE REFILL MODEL
Headline:
Luxury That Lasts.
Instead of discarding your entire brush, simply replace the head every 3 months.
Cleaner. Smarter. Elevated.
Micro-copy:
Refill subscriptions available at launch.
5️⃣ SOCIAL IMPACT (Your 5% Donation Angle)
Headline:
Beauty With Purpose.
5% of profits are donated to organizations chosen by our community.
As a Founder, you help decide where we give.
6️⃣ SOCIAL PROOF (Even Pre-Launch)
You can use:
Dentist credibility statement
~not made yet- will edit in~
Example testimonial style:
“Finally, a toothbrush I don’t want to hide in a drawer.”
7️⃣ FOUNDER CTA SECTION
Headline:
Become a Founding Member.
Be the first to receive:
Early access pricing
Engraving perks
First charity vote
Follow us on:
Instagram
Tiktok
~ don't have these made yet, will add in later~
🎯 Design Direction
Page should feel closer to:
Plumette
Tovane
Hollow
Not:
Denta-K
Minimal navigation.
Lots of white space.
Cream, bone, tortoise, gold tones.
Soft serif typography.
I have attached a picture of the clean vibe I would like- doesn't have to be exact but for inspo
I will also include/add our mock up drawings when they are finished!
Thank you :)

```html
<!DOCTYPE html>
<html lang="en">
<head>
<meta charset="utf-8">
<title>Vörn — Luxury Refillable Toothbrush</title>
<link href="https://fonts.googleapis.com/css2?family=DM+Serif+Display&family=Nunito+Sans:ital,wght@0,400;0,600;0,700;1,400&display=swap" rel="stylesheet">
<style>
:root{
  --tortoise:#A47C5C;
  --tortoise-dark:#8E6A4D;
  --cream:#ECE7DC;
  --ink:#1B1B1B;
  --text:#2E2E2E;
  --muted:#6F6F6F;
  --mist:#F6FBFD;
  --butter:#FFF9D4;
  --gold:#D9B96A;
  --star:#F4A623;
  --white:#FFFFFF;
}
*{margin:0;padding:0;box-sizing:border-box}
html,body{width:1200px;height:3793px;overflow:hidden;background:var(--white)}
body{position:relative;font-family:"Nunito Sans",sans-serif;color:var(--text)}
.serif{font-family:"DM Serif Display",serif}
.abs{position:absolute}
.rule{width:60px;height:3px;background:var(--tortoise);margin:14px auto 0}
.pill{display:inline-block;background:var(--tortoise);color:var(--white);border-radius:30px;font-family:"DM Serif Display",serif}
.photo{position:absolute}

/* header */
.site-header{position:absolute;left:0;top:0;width:1200px;height:85px;background:var(--white)}
.menu-icon{left:112px;top:30px}
.brand{left:0;width:1200px;top:12px;text-align:center;font-size:50px;color:var(--ink);line-height:1}
.contact-btn{left:902px;top:20px;width:118px;height:44px;line-height:44px;text-align:center;font-size:14px;letter-spacing:.5px}
.account-icon{left:1030px;top:30px}
.bag-icon{left:1068px;top:30px}

/* hero */
.hero-photo{left:0;top:85px;width:692px;height:519px;background:linear-gradient(100deg,#A89A8C 0%,#D9CFC7 35%,#EAD2CF 55%,#D2C6BE 80%,#B9ADA2 100%)}
.hero-panel{left:692px;top:85px;width:508px;height:519px;background:var(--cream)}
.hero-title{left:743px;top:172px;font-size:44px;line-height:48px;color:var(--ink)}
.hero-rule{left:745px;top:285px;width:92px;height:3px;background:var(--tortoise)}
.hero-sub{left:745px;top:306px;width:330px;font-size:15px;line-height:23px}
.hero-cta{left:745px;top:372px;width:185px;height:38px;line-height:38px;text-align:center;font-size:15px}
.hero-survey{left:745px;top:432px;font-family:"DM Serif Display",serif;font-style:italic;font-size:15px;color:var(--ink)}
.hero-note{left:745px;top:462px;font-size:13px}

/* problem */
.problem-title{left:0;top:675px;width:1200px;text-align:center;font-size:30px;color:var(--ink)}
.problem-box{left:149px;top:757px;width:902px;height:367px;background:var(--mist);border:2px solid var(--tortoise);border-radius:14px}
.point{position:absolute;display:flex;align-items:center;gap:16px;font-size:17px;line-height:23px;color:var(--ink)}
.point-icon{width:76px;height:76px;border-radius:50%;background:var(--tortoise);box-shadow:-6px -4px 0 -1px var(--white),-7px -5px 0 0 #C9B3A0;flex:none}

/* product band */
.product-band{left:0;top:1214px;width:1200px;height:541px;background:var(--tortoise)}
.product-title{left:112px;top:1298px;font-size:33px;line-height:38px;color:var(--white)}
.product-rule{left:112px;top:1388px;width:64px;height:3px;background:var(--white)}
.product-list{left:112px;top:1412px;width:420px;list-style:none;color:var(--white);font-size:17px;line-height:37.5px}
.product-frame{left:632px;top:1290px;width:464px;height:387px;border:3px solid var(--white);border-radius:12px}
.product-photo{left:645px;top:1300px;width:443px;height:369px;border-radius:10px;background:linear-gradient(120deg,#6E6A66 0%,#B8B4AE 35%,#DCDAD6 55%,#9D9A94 80%,#5F5A55 100%)}

/* refill */
.refill-title{left:0;top:1830px;width:1200px;text-align:center;font-size:30px;color:var(--ink)}
.refill-copy{left:0;top:1901px;width:1200px;text-align:center;font-size:17px;line-height:25px}
.refill-btn{left:446px;top:1968px;width:306px;height:38px;line-height:38px;text-align:center;font-size:15px}

/* purpose */
.purpose-outline{left:1032px;top:2140px;width:50px;height:330px;border:2px solid var(--gold);border-left:none;border-radius:0 12px 12px 0}
.purpose-photo{left:546px;top:2155px;width:529px;height:309px;border-radius:12px;background:linear-gradient(100deg,#C9CCCF 0%,#E9E7E3 40%,#D8C3B1 65%,#A88C78 85%,#C7BBB0 100%)}
.purpose-card{left:125px;top:2078px;width:518px;height:290px;border:2px solid var(--tortoise);border-radius:12px;background:var(--white);padding:8px}
.purpose-inner{width:100%;height:100%;background:var(--butter);border-radius:8px}
.purpose-title{left:171px;top:2122px;font-size:31px;color:var(--ink)}
.purpose-rule{left:171px;top:2170px;width:54px;height:3px;background:var(--tortoise)}
.purpose-item{position:absolute;left:170px;width:420px;font-size:15px;line-height:29px;color:var(--ink);padding-left:22px}
.purpose-item::before{content:"";position:absolute;left:0;top:10px;width:10px;height:10px;border-radius:50%;background:var(--tortoise-dark)}
.badge{left:600px;top:2095px;width:116px;height:116px}
.badge-text{left:600px;top:2122px;width:116px;text-align:center;color:var(--white);font-size:15px;line-height:18px;font-weight:600}
.badge-text b{font-size:22px}

/* testimonials */
.testi-title{left:0;top:2555px;width:1200px;text-align:center;font-size:34px;color:var(--ink)}
.testi-card{width:408px;height:228px;background:var(--white);border-radius:30px;box-shadow:0 4px 14px rgba(0,0,0,.16)}
.testi-avatar{width:116px;height:116px;border-radius:50%;background:radial-gradient(circle at 50% 45%,#D7B8A2 0%,#A77F63 55%,#5F4535 100%);border:4px solid var(--white)}
.quote-mark{font-family:"DM Serif Display",serif;font-size:70px;line-height:1;color:var(--tortoise)}
.testi-quote{width:290px;font-style:italic;font-size:14px;line-height:23.5px;color:var(--muted)}
.testi-name{font-size:16px;font-weight:700;color:var(--ink)}
.testi-stars{color:var(--star);font-size:17px;letter-spacing:1px}

/* founding */
.founding-band{left:0;top:2990px;width:1200px;height:410px;background:var(--tortoise)}
.founding-title{left:0;top:3063px;width:1200px;text-align:center;font-size:34px;color:var(--white)}
.founding-rule{left:571px;top:3112px;width:58px;height:3px;background:var(--white)}
.perk-line{left:340px;top:3208px;width:530px;border-top:2px dotted rgba(255,255,255,.8)}
.perk-circle{width:112px;height:112px;border-radius:50%;background:var(--white);border:6px solid #E9DCCF}
.perk-label{width:240px;text-align:center;font-family:"DM Serif Display",serif;font-size:19px;color:var(--white)}

/* footer */
.footer-brand{left:160px;top:3486px;font-size:70px;color:var(--ink);line-height:1}
.social-dot{width:32px;height:32px;border-radius:50%;border:1.5px solid #555}
.foot-col h4{font-size:16px;font-weight:700;color:var(--ink);margin-bottom:20px}
.foot-col li{list-style:none;font-size:13.5px;color:#4D4D4D;line-height:26px}
.contact-item{position:absolute;left:873px;font-size:13px;color:#4D4D4D;line-height:18px}
.contact-item strong{display:block;font-size:11.5px;color:var(--ink)}
.foot-rule{left:108px;top:3710px;width:984px;border-top:1px solid #DDD}
.copyright{left:0;top:3737px;width:1200px;text-align:center;font-size:15px;color:#555}
.to-top{left:1104px;top:3693px;width:36px;height:36px;border-radius:50%;background:var(--tortoise)}
</style>
</head>
<body>

<header class="site-header">
  <svg class="abs menu-icon" width="32" height="26" viewBox="0 0 32 26"><g stroke="#1B1B1B" stroke-width="3" stroke-linecap="round"><line x1="2" y1="3" x2="30" y2="3"/><line x1="2" y1="13" x2="24" y2="13"/><line x1="2" y1="23" x2="30" y2="23"/></g></svg>
  <div class="abs brand serif">vörn</div>
  <a class="abs pill contact-btn">CONTACT US</a>
  <svg class="abs account-icon" width="28" height="28" viewBox="0 0 28 28" fill="none" stroke="#1B1B1B" stroke-width="2"><circle cx="14" cy="14" r="12"/><circle cx="14" cy="11" r="4.5"/><path d="M6 22c2-4 5-5.5 8-5.5s6 1.5 8 5.5"/></svg>
  <svg class="abs bag-icon" width="22" height="28" viewBox="0 0 22 28" fill="none" stroke="#1B1B1B" stroke-width="2"><rect x="2" y="9" width="18" height="17" rx="1"/><path d="M6 11V6a5 5 0 0 1 10 0v5"/></svg>
</header>

<section>
  <div class="photo hero-photo" role="img" aria-label="Blush pink electric toothbrush standing on a vanity beside white flowers and a wooden brush"></div>
  <div class="abs hero-panel"></div>
  <h1 class="abs hero-title serif">Rethink Your<br>Daily Hollow</h1>
  <div class="abs hero-rule"></div>
  <p class="abs hero-sub">A luxury, refillable toothbrush designed with intention — where beauty meets dentistry.</p>
  <a class="abs pill hero-cta">Join the Founding List</a>
  <p class="abs hero-survey">Complete survey for 20% off first purchase</p>
  <p class="abs hero-note">Launching Fall 2026 · Limited Keeper’s Edition</p>
</section>

<section>
  <h2 class="abs problem-title serif">Oral Care hasn’t Evolved like Beauty has.<div class="rule"></div></h2>
  <div class="abs problem-box"></div>
  <div class="point" style="left:184px;top:794px"><span class="point-icon" role="img" aria-label="Skincare icon"></span>We invest in skincare rituals.</div>
  <div class="point" style="left:710px;top:800px"><span class="point-icon" role="img" aria-label="Bathtub icon"></span>We curate our bathrooms.</div>
  <div class="point" style="left:184px;top:902px"><span class="point-icon" role="img" aria-label="Package icon"></span>We obsess over packaging and detail.</div>
  <div class="point" style="left:710px;top:908px"><span class="point-icon" role="img" aria-label="Toothbrush icon"></span>Yet the toothbrush</div>
  <div class="point" style="left:184px;top:1006px"><span class="point-icon" role="img" aria-label="Tooth icon"></span>Something we use twice daily — remains<br>clinical, disposable, and uninspired.</div>
  <div class="point" style="left:710px;top:1011px"><span class="point-icon" role="img" aria-label="Dental care icon"></span>You deserve better.</div>
</section>

<section>
  <div class="abs product-band"></div>
  <h2 class="abs product-title serif">Designed to be Displayed<br>Engineered to Perform</h2>
  <div class="abs product-rule"></div>
  <ul class="abs product-list">
    <li>• Hand-finished premium prints on an acetate handle</li>
    <li>• Slim sculptural silhouette</li>
    <li>• Gold-accent detailing</li>
    <li>• Replaceable brush head system</li>
    <li>• Premium bristles (dentist-selected)</li>
    <li>• Designed by a practicing dentist</li>
  </ul>
  <div class="abs product-frame"></div>
  <div class="photo product-photo" role="img" aria-label="White toothbrush on a bathroom counter beside a stone basin and window"></div>
</section>

<section>
  <h2 class="abs refill-title serif">Luxury That Lasts<div class="rule"></div></h2>
  <p class="abs refill-copy">Instead of discarding your entire brush, simply replace the head every 3 months.<br>Cleaner. Smarter. Elevated.</p>
  <a class="abs pill refill-btn">Refill subscriptions available at launch</a>
</section>

<section>
  <div class="abs purpose-outline"></div>
  <div class="photo purpose-photo" role="img" aria-label="Smiling woman brushing her teeth in a bright bathroom beside a round mirror"></div>
  <div class="abs purpose-card"><div class="purpose-inner"></div></div>
  <h2 class="abs purpose-title serif">Beauty With Purpose</h2>
  <div class="abs purpose-rule"></div>
  <p class="purpose-item" style="top:2198px">5% of profits are donated to organizations chosen by our community.</p>
  <p class="purpose-item" style="top:2286px">As a Founder, you help decide where we give.</p>
  <svg class="abs badge" viewBox="0 0 116 116"><circle cx="58" cy="58" r="56" fill="#8E6A4D"/><circle cx="58" cy="58" r="50" fill="none" stroke="#fff" stroke-width="1.5" stroke-dasharray="3 4"/></svg>
  <div class="abs badge-text">Your <b>5%</b><br>Donation<br>Angle</div>
</section>

<section>
  <h2 class="abs testi-title serif">Testimonials<div class="rule"></div></h2>
  <svg class="abs" style="left:42px;top:2752px" width="22" height="36" viewBox="0 0 22 36"><path d="M18 3 4 18l14 15" fill="none" stroke="#222" stroke-width="4" stroke-linecap="round"/></svg>
  <svg class="abs" style="left:1136px;top:2752px" width="22" height="36" viewBox="0 0 22 36"><path d="M4 3l14 15L4 33" fill="none" stroke="#222" stroke-width="4" stroke-linecap="round"/></svg>

  <div class="abs testi-card" style="left:178px;top:2657px"></div>
  <div class="abs testi-avatar" role="img" aria-label="Customer portrait" style="left:124px;top:2711px"></div>
  <div class="abs quote-mark" style="left:278px;top:2680px">“</div>
  <p class="abs testi-quote" style="left:281px;top:2731px">“Finally, a toothbrush I don’t want to hide in a drawer.Elegant enough for my vanity. Effective enough for my dentist.”</p>
  <p class="abs testi-name" style="left:280px;top:2816px">John Doe</p>
  <p class="abs testi-stars" style="left:279px;top:2836px">★★★★★</p>

  <div class="abs testi-card" style="left:667px;top:2657px"></div>
  <div class="abs testi-avatar" role="img" aria-label="Customer portrait" style="left:613px;top:2711px"></div>
  <div class="abs quote-mark" style="left:767px;top:2680px">“</div>
  <p class="abs testi-quote" style="left:770px;top:2731px">“Finally, a toothbrush I don’t want to hide in a drawer.Elegant enough for my vanity. Effective enough for my dentist.”</p>
  <p class="abs testi-name" style="left:769px;top:2816px">John Doe</p>
  <p class="abs testi-stars" style="left:768px;top:2836px">★★★★★</p>
</section>

<section>
  <div class="abs founding-band"></div>
  <h2 class="abs founding-title serif">Become a Founding Member</h2>
  <div class="abs founding-rule"></div>
  <div class="abs perk-line"></div>
  <div class="abs perk-circle" role="img" aria-label="Price tag icon" style="left:225px;top:3153px"></div>
  <div class="abs perk-circle" role="img" aria-label="Engraving tool icon" style="left:549px;top:3153px"></div>
  <div class="abs perk-circle" role="img" aria-label="Heart in hand icon" style="left:871px;top:3153px"></div>
  <p class="abs perk-label" style="left:161px;top:3290px">Early access pricing</p>
  <p class="abs perk-label" style="left:485px;top:3290px">Engraving perks</p>
  <p class="abs perk-label" style="left:807px;top:3290px">First charity vote</p>
</section>

<footer>
  <div class="abs footer-brand serif">vörn</div>
  <div class="abs social-dot" style="left:191px;top:3583px"></div>
  <div class="abs social-dot" style="left:232px;top:3583px"></div>

  <div class="abs foot-col" style="left:433px;top:3478px">
    <h4>Quick Links</h4>
    <ul><li>Home</li><li>Services</li><li>Products</li><li>About Us</li><li>Blog</li><li>Contact Us</li></ul>
  </div>
  <div class="abs foot-col" style="left:615px;top:3478px">
    <h4>About Company</h4>
    <ul><li>Terms &amp; Conditions</li><li>Privacy Policy</li><li>Support</li><li>Site Map</li><li>FAQ</li></ul>
  </div>
  <div class="abs foot-col" style="left:851px;top:3478px"><h4>Contact Us</h4></div>

  <svg class="abs" style="left:849px;top:3523px" width="14" height="14" viewBox="0 0 24 24"><path fill="#A47C5C" d="M6.6 10.8a15 15 0 0 0 6.6 6.6l2.2-2.2c.3-.3.7-.4 1-.2 1.1.4 2.3.6 3.6.6.6 0 1 .4 1 1V20c0 .6-.4 1-1 1A17 17 0 0 1 3 4c0-.6.4-1 1-1h3.5c.6 0 1 .4 1 1 0 1.3.2 2.5.6 3.6.1.3 0 .7-.2 1z"/></svg>
  <p class="contact-item" style="top:3520px"><strong>Phone</strong>+1 (555) 014 2290</p>
  <svg class="abs" style="left:847px;top:3574px" width="16" height="13" viewBox="0 0 16 13"><rect width="16" height="13" rx="1.5" fill="#A47C5C"/><path d="M1 1.5 8 7l7-5.5" fill="none" stroke="#fff" stroke-width="1.3"/></svg>
  <p class="contact-item" style="top:3571px"><strong>Email</strong>hello@vörn.com</p>
  <svg class="abs" style="left:850px;top:3624px" width="11" height="15" viewBox="0 0 12 16"><path fill="#A47C5C" d="M6 0a6 6 0 0 0-6 6c0 4.5 6 10 6 10s6-5.5 6-10a6 6 0 0 0-6-6zm0 8.2A2.2 2.2 0 1 1 6 3.8a2.2 2.2 0 0 1 0 4.4z"/></svg>
  <p class="contact-item" style="top:3622px"><strong>Location</strong>Linden Row. 82 Harbor Ave,<br>NY 10200, USA</p>

  <div class="abs foot-rule"></div>
  <p class="abs copyright">2026 Copyrights -  Vörn | All Rights Reserved</p>
  <div class="abs to-top"><svg width="36" height="36" viewBox="0 0 36 36"><path d="M12 21l6-6 6 6" fill="none" stroke="#fff" stroke-width="2.2" stroke-linecap="round"/></svg></div>
</footer>

</body>
</html>
```